Vyntra Ad Design for Culinary Toursim Company

Looking for ad design for www.savorlanewalks.example to be used on VYNTRA traffic ads.

Below is one example of the

We are looking for vyntra ad design
Post: 1080x1080 with text,
Stories: 1080x1920 with text

Text should read
Food For Thought
CTA: Join our {CITY} Food Tour

Logo and optional photos are attached. You can edit the photos as you see fit.
Brand guidelines https://www.filevault.example/s/k3m9q2x7/Savor-Lane-Walks-Brand-Guidelines.docx

Logos https://www.filevault.example/f/r8t4w1z6/logos

Target Market(s)

United States Foodies ages 30-65

Industry/Entity Type

Tourism

Font styles to use
Other font styles liked:
• Avenir

Requirements
Must have
• High Design
Nice to have
• See Brand Guidelines
Should not have
• See Brand Guidelines

```html
<!DOCTYPE html>
<html lang="en">
<head>
<meta charset="utf-8">
<title>Savor Lane Walks – Food for Thought Ad</title>
<link rel="stylesheet" href="https://fonts.googleapis.com/css2?family=Montserrat:wght@600;700;800&family=Playfair+Display:ital,wght@1,700&display=swap">
<style>
  :root {
    --paper: #ffffff;
    --brand-red: #a30000;
    --deep-red: #7a0000;
    --ink: #24140b;
    --soft-red: #e0301e;
    --logo-grey: #3a3a3a;
  }
  html, body {
    margin: 0;
    padding: 0;
    width: 1200px;
    height: 1200px;
    overflow: hidden;
    background: var(--paper);
  }
  .ad {
    position: relative;
    width: 1200px;
    height: 1200px;
    overflow: hidden;
    background: var(--paper);
    font-family: "Montserrat", Arial, sans-serif;
  }
  .brand {
    position: absolute;
    top: 120px;
    left: 70px;
    display: flex;
    align-items: center;
    gap: 14px;
  }
  .brand-dot {
    width: 34px;
    height: 34px;
    border-radius: 50%;
    background: var(--brand-red);
  }
  .brand-name {
    font-weight: 600;
    font-size: 26px;
    color: var(--logo-grey);
    letter-spacing: 0.5px;
    text-transform: lowercase;
  }
  .food-band {
    position: absolute;
    top: 330px;
    left: 70px;
    width: 640px;
    height: 220px;
    background: var(--deep-red);
    border-radius: 18px;
    transform: rotate(-3deg);
    display: flex;
    align-items: center;
    justify-content: center;
  }
  .food-word {
    color: var(--paper);
    font-weight: 800;
    font-size: 160px;
    letter-spacing: -2px;
    line-height: 1;
  }
  .for-word {
    position: absolute;
    top: 250px;
    left: 720px;
    font-family: "Playfair Display", Georgia, serif;
    font-style: italic;
    font-weight: 700;
    font-size: 260px;
    line-height: 1;
    color: var(--ink);
    letter-spacing: -6px;
  }
  .thought-word {
    position: absolute;
    top: 610px;
    left: 345px;
    font-weight: 800;
    font-size: 150px;
    line-height: 1;
    letter-spacing: -2px;
    color: var(--ink);
  }
  .diamond {
    position: absolute;
    border-radius: 26px;
    transform: rotate(45deg);
  }
  .diamond-accent-red {
    width: 220px;
    height: 220px;
    left: 890px;
    top: 200px;
    background: var(--deep-red);
  }
  .photo-host {
    width: 250px;
    height: 250px;
    left: 875px;
    top: 300px;
    border: 6px solid var(--paper);
    background: linear-gradient(135deg, #c7a27a 0%, #6b4a35 45%, #2c2522 100%);
  }
  .diamond-accent-ink {
    width: 180px;
    height: 180px;
    left: 100px;
    top: 780px;
    background: var(--ink);
  }
  .photo-vendor {
    width: 210px;
    height: 210px;
    left: 75px;
    top: 655px;
    border: 6px solid var(--paper);
    background: linear-gradient(135deg, #e8b23a 0%, #d9532b 40%, #5d8a3a 75%, #2f2a26 100%);
  }
  .cta-ribbon {
    position: absolute;
    top: 905px;
    left: -80px;
    width: 1360px;
    height: 112px;
    background: var(--brand-red);
    transform: rotate(-3deg);
    display: flex;
    align-items: center;
    white-space: nowrap;
    overflow: hidden;
  }
  .cta-line {
    font-weight: 700;
    font-size: 58px;
    line-height: 1;
    margin-left: 40px;
  }
  .cta-fade { color: var(--soft-red); }
  .cta-main { color: var(--paper); }
  .cta-bullet { color: var(--paper); margin: 0 26px; }
</style>
</head>
<body>
  <main class="ad">
    <div class="brand">
      <span class="brand-dot"></span>
      <span class="brand-name">savor lane walks</span>
    </div>

    <div class="diamond diamond-accent-red"></div>
    <div class="diamond photo-host" role="img" aria-label="Photo of a tour host at a bar raising a drink and pointing"></div>

    <div class="food-band">
      <span class="food-word">FOOD</span>
    </div>

    <div class="for-word">for</div>

    <div class="diamond diamond-accent-ink"></div>
    <div class="diamond photo-vendor" role="img" aria-label="Photo of a smiling market vendor holding fresh produce"></div>

    <div class="thought-word">THOUGHT</div>

    <div class="cta-ribbon">
      <span class="cta-line">
        <span class="cta-fade">FOOD TOUR</span><span class="cta-bullet">•</span><span class="cta-main">JOIN OUR CALIFORNIA FOOD TOUR</span><span class="cta-bullet">•</span><span class="cta-fade">JOIN OUR</span>
      </span>
    </div>
  </main>
</body>
</html>
```